Business card design for a content marketing agency

Need a business card design suitable for a digital marketing agency. Needs to be a bold and creative, high quality design that exudes expertise and professionalism, and instills in prospective new customers a sense of confidence that we are the right company to do business with. Specifications must meet PrintNorvo requirement for extra thick matte stock. Needs to incorporate logo, tagline, name, title, website url, address, city, state, zip code, and mobile number.. I spec'd s single side design but I'm to a double sided design if it's strong and compelling. I like the use of icons associated with contact info, but it's not a requirement. Mostly, the design needs to command attention because it's so good or unusual. I have all kinds of files in large thru small sizes in jpg andpgn. pick from what you need, and let me know if you have questions.

Target Market(s)

CEO, Mktg VP's and small to medium size tech and prof'l service businesses

Industry/Entity Type

Marketing

Contact Information for Business Card

Perry Lindqvist
Chief Executive Officer
418 Wexcombe Lane
Larkfield, OR 97099
perry@quelmarketing.example
www.quelmarketing.example
541-555-2716

Font styles to use
Sans Serif

Colors
0692cd
9bcb3c

Requirements
Must have
• Tagline is "Growth That Clients Can Rely On".
• Needs to be a bold and creative, high quality design that exudes expertise and professionalism, and instills in prospective new customers a sense of confidence that we are the right company to do business with. Specifications must meet PrintNorvo requirement for extra thick matte stock. Needs to incorporate logo, tagline, name, title, website url, address, city, state, zip code, and mobile number..
Nice to have
• I spec'd s single side design but I'm open to a double sided design if it's strong and compelling. I like the use of icons associated with contact info, but it's not a requirement.
Should not have
• Chose colors that are the same and/or compatible with colors in the logo

```html
<!DOCTYPE html>
<html lang="en">
<head>
<meta charset="utf-8">
<title>Quel Marketing – Business Card</title>
<link rel="stylesheet" href="https://fonts.googleapis.com/css2?family=Open+Sans:wght@300;400;600;700&family=Arimo:wght@400;700&display=swap">
<style>
  :root {
    --brand-blue: #0692cd;
    --brand-green: #9bcb3c;
    --card-white: #ffffff;
    --card-black: #111111;
    --band-edge: #e4e4e4;
    --backdrop: #2b2b2d;
  }
  * { box-sizing: border-box; margin: 0; padding: 0; }
  html, body { width: 1200px; height: 800px; overflow: hidden; }
  body {
    background: var(--backdrop);
    display: flex;
    align-items: center;
    justify-content: center;
    gap: 40px;
    font-family: "Arimo", sans-serif;
  }
  .card {
    position: relative;
    width: 540px;
    height: 309px;
    overflow: hidden;
    box-shadow: 0 10px 28px rgba(0,0,0,.45);
  }

  /* Front */
  .card--front { background: var(--card-white); }
  .wordmark {
    display: flex;
    align-items: center;
    gap: 10px;
    font-family: "Open Sans", sans-serif;
    font-weight: 600;
    white-space: nowrap;
  }
  .card--front .wordmark {
    position: absolute;
    left: 34px; top: 38px;
    font-size: 28px;
    color: var(--brand-blue);
  }
  .wordmark__square {
    width: 22px; height: 22px;
    background: currentColor;
  }
  .person {
    position: absolute;
    right: 36px; top: 96px;
  }
  .person__name {
    font-weight: 700;
    font-size: 25px;
    letter-spacing: .5px;
    color: var(--brand-blue);
    text-transform: uppercase;
    line-height: 1;
    white-space: nowrap;
  }
  .person__title {
    margin-top: 4px;
    font-size: 11.5px;
    color: var(--brand-green);
    text-transform: uppercase;
    letter-spacing: .3px;
  }
  .tagline-band {
    position: absolute;
    left: 0; right: 0;
    top: 146px; height: 62px;
    background: var(--brand-green);
    border-top: 5px solid var(--band-edge);
    border-bottom: 5px solid var(--band-edge);
    display: flex;
    align-items: center;
    padding-left: 30px;
  }
  .tagline {
    font-family: "Open Sans", sans-serif;
    font-weight: 300;
    font-size: 27px;
    color: var(--card-white);
    text-transform: uppercase;
    white-space: nowrap;
    letter-spacing: -.3px;
  }
  .contact {
    position: absolute;
    left: 30px; top: 226px;
    list-style: none;
  }
  .contact__item {
    display: flex;
    align-items: center;
    gap: 8px;
    font-size: 11px;
    color: var(--brand-blue);
    text-transform: uppercase;
    line-height: 16px;
    white-space: nowrap;
  }
  .contact__item--phone {
    font-size: 15px;
    font-weight: 700;
    color: var(--brand-green);
    line-height: 20px;
  }
  .icon { width: 12px; height: 12px; flex: none; }
  .address {
    position: absolute;
    left: 330px; top: 248px;
    display: flex;
    gap: 8px;
    font-style: normal;
    font-size: 11.5px;
    line-height: 16px;
    color: var(--brand-blue);
    text-transform: uppercase;
    white-space: nowrap;
  }
  .address .icon { width: 13px; height: 16px; }

  /* Back */
  .card--back {
    background: var(--card-black);
    display: flex;
    align-items: center;
    justify-content: center;
  }
  .card--back .wordmark {
    font-size: 36px;
    color: var(--card-white);
    gap: 14px;
  }
  .card--back .wordmark__square { width: 28px; height: 28px; }
</style>
</head>
<body>

  <section class="card card--front" aria-label="Business card, front">
    <div class="wordmark"><span class="wordmark__square"></span>Quel Marketing</div>

    <div class="person">
      <p class="person__name">Perry Lindqvist</p>
      <p class="person__title">Chief Executive Officer</p>
    </div>

    <div class="tagline-band">
      <p class="tagline">Growth That Clients Can Rely On</p>
    </div>

    <ul class="contact">
      <li class="contact__item contact__item--phone">
        <svg class="icon" viewBox="0 0 24 24" fill="var(--brand-green)"><path d="M6.6 10.8a15.1 15.1 0 0 0 6.6 6.6l2.2-2.2a1 1 0 0 1 1-.25 11.4 11.4 0 0 0 3.6.57 1 1 0 0 1 1 1V20a1 1 0 0 1-1 1A17 17 0 0 1 3 4a1 1 0 0 1 1-1h3.5a1 1 0 0 1 1 1c0 1.25.2 2.45.57 3.57a1 1 0 0 1-.25 1z"/></svg>
        541-555-2716
      </li>
      <li class="contact__item">
        <svg class="icon" viewBox="0 0 24 24" fill="none" stroke="var(--brand-green)" stroke-width="2.2"><rect x="2" y="5" width="20" height="14" rx="1"/><path d="M2 6l10 7 10-7"/></svg>
        perry@quelmarketing.example
      </li>
      <li class="contact__item">
        <svg class="icon" viewBox="0 0 24 24" fill="none" stroke="var(--brand-green)" stroke-width="2"><circle cx="12" cy="12" r="10"/><path d="M2 12h20M12 2c3 3 3 17 0 20M12 2c-3 3-3 17 0 20"/></svg>
        www.quelmarketing.example
      </li>
    </ul>

    <address class="address">
      <svg class="icon" viewBox="0 0 24 30" fill="var(--brand-green)"><path d="M12 0a11 11 0 0 0-11 11c0 8 11 19 11 19s11-11 11-19A11 11 0 0 0 12 0zm0 15a4 4 0 1 1 0-8 4 4 0 0 1 0 8z"/></svg>
      <span>418 Wexcombe Lane<br>Larkfield, OR 97099</span>
    </address>
  </section>

  <section class="card card--back" aria-label="Business card, back">
    <div class="wordmark"><span class="wordmark__square"></span>Quel Marketing</div>
  </section>

</body>
</html>
```